Updated Stationary needed using new logo for Hair Tissue Mineral Analysis Company

Simple stationary design needed using new logo!
1. 8.5" x 11" Letterhead with company information listed below
2. 8.5" x 11" Design with Footer only with logo and information for print materials
3. 5.5" x 8.5" letterhead design
4. 4.125" x 9.5" Business envelope (#10 envelope) with address
5. 4.125" x 9.5" Business envelope with clear window (#10 envelope) with address
6. 6.5" x 9.5" envelope (6 3/4 Booklet envelope) with address
7. 10" x 13" Open End envelope
Address:
4817 N. Corwin Street
Phoenix, AZ 85021
Phone:
(602)-417-3926
Website:
www.pexumor.com
Email:
information@pexumor.com
Updates
Need extra days to review
Focused on completing other projects first
Look and feel
Each slider illustrates characteristics of the customer's brand and the style your logo design should communicate.

```html
<!DOCTYPE html>
<html lang="en">
<head>
<meta charset="utf-8">
<title>Pexumor Labs — Stationery Suite</title>
<link rel="stylesheet" href="https://fonts.googleapis.com/css2?family=Michroma&family=Outfit:wght@400&display=swap">
<style>
  :root {
    --board: #f4f4f4;
    --paper: #ffffff;
    --brand-blue: #2d55a4;
    --brand-blue-light: #3f6fcc;
    --accent-orange: #ef8427;
    --ink: #1d2740;
    --navy: #0c1838;
    --night: #0b111e;
    --glow-blue: #2b5fc4;
    --mist-blue: #dfe8fa;
    --wave-red: #e8333f;
  }
  * { box-sizing: border-box; margin: 0; padding: 0; }
  html, body { width: 1200px; height: 2161px; overflow: hidden; background: var(--board); }
  .board {
    position: relative; width: 1430px; height: 2576px;
    transform: scale(0.83916); transform-origin: 0 0;
  }
  .sheet { position: absolute; overflow: hidden; }
  .sheet--paper { background: var(--paper); }
  .sheet--navy { background: var(--navy); }
  .sheet--glow { background: linear-gradient(150deg, var(--night) 0%, #111a30 45%, #1c3570 75%, var(--glow-blue) 100%); }
  .sheet--lifted { box-shadow: 0 12px 30px rgba(0,0,0,.28); }

  .brand {
    position: absolute; display: flex; align-items: center; gap: .35em;
    font-family: "Michroma", sans-serif; font-weight: 400;
    color: var(--brand-blue); letter-spacing: .04em; white-space: nowrap; line-height: 1;
  }
  .brand::before {
    content: ""; width: .42em; height: .42em; border-radius: 50%;
    background: var(--accent-orange); flex: none;
  }
  .brand--on-dark { color: var(--brand-blue-light); }

  .contact {
    position: absolute; font-family: "Outfit", sans-serif; color: var(--ink);
    line-height: 1.4; width: 36em; height: 3em;
  }
  .contact--on-dark { color: #ffffff; }
  .contact__item { position: absolute; top: 0; padding-left: 1.35em; white-space: nowrap; }
  .contact__item svg { position: absolute; left: 0; width: .95em; height: .95em; fill: var(--accent-orange); }
  .contact__item--address { left: 0; }
  .contact__item--phone { left: 14.2em; }
  .contact__item--email { left: 24.6em; }
  .contact__icon-1 { top: .25em; }
  .contact__icon-2 { top: 1.65em; }

  .deco { position: absolute; }
  .deco--hex-orange { background: radial-gradient(ellipse at 35% 45%, rgba(239,132,39,.22), rgba(239,132,39,0) 70%); }
  .deco--hex-blue { background: radial-gradient(ellipse at 60% 50%, rgba(120,150,215,.22), rgba(120,150,215,0) 70%); }
  .deco--hex-red { background: radial-gradient(ellipse at 40% 45%, rgba(200,50,60,.28), rgba(200,50,60,0) 70%); }
  .deco--hex-night { background: radial-gradient(ellipse at 60% 50%, rgba(40,80,180,.35), rgba(40,80,180,0) 70%); }
  .deco--wave { background: radial-gradient(ellipse at 55% 50%, rgba(232,51,63,.55), rgba(232,51,63,0) 70%); }

  .curve { position: absolute; left: 0; top: 0; }
</style>
</head>
<body>
<svg width="0" height="0" style="position:absolute">
  <defs>
    <symbol id="i-pin" viewBox="0 0 16 16"><path d="M8 0a5.5 5.5 0 0 0-5.5 5.5C2.5 9.7 8 16 8 16s5.5-6.3 5.5-10.5A5.5 5.5 0 0 0 8 0zm0 7.7a2.2 2.2 0 1 1 0-4.4 2.2 2.2 0 0 1 0 4.4z"/></symbol>
    <symbol id="i-phone" viewBox="0 0 16 16"><path d="M3.6 1 6 3.8 4.8 6a9.5 9.5 0 0 0 5.2 5.2L12.2 10 15 12.4 13.3 15C6.6 14.6 1.4 9.4 1 2.7z"/></symbol>
    <symbol id="i-mail" viewBox="0 0 16 16"><path d="M1 3h14v1.4L8 9 1 4.4zM1 6.2l7 4.6 7-4.6V13H1z"/></symbol>
    <symbol id="i-cursor" viewBox="0 0 16 16"><path d="M3 1l10 8.5-4.3.5 2.6 4.8-1.9 1-2.6-4.8L3 14z"/></symbol>
    <linearGradient id="mistBand" x1="0" y1="1" x2="1" y2="0"><stop offset="0" stop-color="#dfe8fa"/><stop offset="1" stop-color="#e9effc"/></linearGradient>
    <linearGradient id="nightBand" x1="0" y1="1" x2="1" y2="0"><stop offset="0" stop-color="#3a63b8" stop-opacity=".35"/><stop offset="1" stop-color="#3f74d8" stop-opacity=".9"/></linearGradient>
  </defs>
</svg>

<main class="board">

  <!-- Footer-only sheet -->
  <section class="sheet sheet--paper" style="left:59px;top:58px;width:649px;height:840px">
    <div class="deco deco--hex-orange" role="img" aria-label="Faint orange hexagonal molecule pattern" style="left:0;top:50px;width:250px;height:275px"></div>
    <div class="deco deco--hex-blue" role="img" aria-label="Faint blue hexagonal molecule pattern" style="left:410px;top:772px;width:239px;height:68px"></div>
    <div class="brand" style="left:49px;top:626px;font-size:44px">PEXUMOR LABS</div>
    <div class="contact" style="left:49px;top:726px;font-size:14.5px">
      <div class="contact__item contact__item--address"><svg class="contact__icon-1"><use href="#i-pin"/></svg>4817 N. Corwin Street<br>Phoenix, AZ 85021</div>
      <div class="contact__item contact__item--phone"><svg class="contact__icon-1"><use href="#i-phone"/></svg><svg class="contact__icon-2"><use href="#i-cursor"/></svg>602-417-3926<br>www.pexumor.com</div>
      <div class="contact__item contact__item--email"><svg class="contact__icon-1"><use href="#i-mail"/></svg>information@pexumor.com</div>
    </div>
  </section>

  <!-- Full letterhead -->
  <section class="sheet sheet--paper" style="left:724px;top:58px;width:649px;height:840px">
    <svg class="curve" width="649" height="840">
      <path d="M0 840 Q130 660 649 655 L649 660 Q250 680 95 840 Z" fill="url(#mistBand)"/>
      <path d="M296 178 Q500 182 649 137 L649 170 Q480 200 296 180 Z" fill="var(--accent-orange)"/>
    </svg>
    <div class="deco deco--hex-orange" role="img" aria-label="Faint orange hexagonal molecule pattern" style="left:0;top:147px;width:235px;height:220px"></div>
    <div class="deco deco--hex-blue" role="img" aria-label="Faint blue hexagonal molecule pattern" style="left:455px;top:445px;width:194px;height:190px"></div>
    <div class="brand" style="left:51px;top:80px;font-size:44px">PEXUMOR LABS</div>
    <div class="contact" style="left:50px;top:718px;font-size:14.5px">
      <div class="contact__item contact__item--address"><svg class="contact__icon-1"><use href="#i-pin"/></svg>4817 N. Corwin Street<br>Phoenix, AZ 85021</div>
      <div class="contact__item contact__item--phone"><svg class="contact__icon-1"><use href="#i-phone"/></svg><svg class="contact__icon-2"><use href="#i-cursor"/></svg>602-417-3926<br>www.pexumor.com</div>
      <div class="contact__item contact__item--email"><svg class="contact__icon-1"><use href="#i-mail"/></svg>information@pexumor.com</div>
    </div>
  </section>

  <!-- Envelope with return address -->
  <section class="sheet sheet--glow" style="left:59px;top:915px;width:649px;height:289px">
    <svg class="curve" width="649" height="289">
      <path d="M0 289 Q190 100 649 105 L649 109 Q300 112 92 289 Z" fill="url(#nightBand)"/>
    </svg>
    <div class="brand brand--on-dark" style="left:61px;top:50px;font-size:18px">PEXUMOR LABS</div>
    <div class="contact contact--on-dark" style="left:61px;top:87px;font-size:5.5px">
      <div class="contact__item contact__item--address"><svg class="contact__icon-1"><use href="#i-pin"/></svg>4817 N. Corwin Street<br>Phoenix, AZ 85021</div>
      <div class="contact__item contact__item--phone"><svg class="contact__icon-1"><use href="#i-phone"/></svg><svg class="contact__icon-2"><use href="#i-cursor"/></svg>602-417-3926<br>www.pexumor.com</div>
      <div class="contact__item contact__item--email"><svg class="contact__icon-1"><use href="#i-mail"/></svg>information@pexumor.com</div>
    </div>
  </section>

  <!-- Envelope back -->
  <section class="sheet sheet--glow" style="left:724px;top:915px;width:649px;height:289px">
    <div class="brand brand--on-dark" style="left:61px;top:200px;font-size:33px">PEXUMOR LABS</div>
  </section>

  <!-- Booklet envelope back -->
  <section class="sheet sheet--navy" style="left:59px;top:1220px;width:649px;height:437px">
    <div class="deco deco--hex-red" role="img" aria-label="Faint red hexagonal molecule pattern" style="left:0;top:10px;width:235px;height:210px"></div>
    <div class="deco deco--hex-night" role="img" aria-label="Faint blue hexagonal molecule pattern" style="left:490px;top:280px;width:159px;height:157px"></div>
    <div class="brand brand--on-dark" style="left:51px;top:326px;font-size:34px">PEXUMOR LABS</div>
  </section>

  <!-- Booklet envelope front -->
  <section class="sheet sheet--navy" style="left:724px;top:1220px;width:649px;height:437px">
    <div class="deco deco--wave" role="img" aria-label="Flowing red line-wave graphic" style="left:285px;top:0;width:364px;height:305px"></div>
    <div class="deco deco--hex-night" role="img" aria-label="Faint blue hexagonal molecule pattern" style="left:470px;top:0;width:179px;height:130px"></div>
    <div class="deco deco--hex-red" role="img" aria-label="Faint red hexagonal molecule pattern" style="left:0;top:325px;width:120px;height:112px"></div>
    <div class="brand brand--on-dark" style="left:51px;top:226px;font-size:34px">PEXUMOR LABS</div>
    <div class="contact contact--on-dark" style="left:50px;top:285px;font-size:10.5px">
      <div class="contact__item contact__item--address"><svg class="contact__icon-1"><use href="#i-pin"/></svg>4817 N. Corwin Street<br>Phoenix, AZ 85021</div>
      <div class="contact__item contact__item--phone"><svg class="contact__icon-1"><use href="#i-phone"/></svg><svg class="contact__icon-2"><use href="#i-cursor"/></svg>602-417-3926<br>www.pexumor.com</div>
      <div class="contact__item contact__item--email"><svg class="contact__icon-1"><use href="#i-mail"/></svg>information@pexumor.com</div>
    </div>
  </section>

  <!-- Half letterhead -->
  <section class="sheet sheet--paper sheet--lifted" style="left:640px;top:1608px;width:702px;height:909px">
    <svg class="curve" width="702" height="909">
      <path d="M0 909 Q150 710 702 702 L702 708 Q270 730 100 909 Z" fill="url(#mistBand)"/>
      <path d="M320 195 Q540 200 702 148 L702 185 Q520 220 320 197 Z" fill="var(--accent-orange)"/>
    </svg>
    <div class="deco deco--hex-orange" role="img" aria-label="Faint orange hexagonal molecule pattern" style="left:0;top:162px;width:250px;height:125px"></div>
    <div class="deco deco--hex-blue" role="img" aria-label="Faint blue hexagonal molecule pattern" style="left:495px;top:480px;width:207px;height:205px"></div>
    <div class="brand" style="left:53px;top:95px;font-size:48px">PEXUMOR LABS</div>
    <div class="contact" style="left:53px;top:777px;font-size:15.5px">
      <div class="contact__item contact__item--address"><svg class="contact__icon-1"><use href="#i-pin"/></svg>4817 N. Corwin Street<br>Phoenix, AZ 85021</div>
      <div class="contact__item contact__item--phone"><svg class="contact__icon-1"><use href="#i-phone"/></svg><svg class="contact__icon-2"><use href="#i-cursor"/></svg>602-417-3926<br>www.pexumor.com</div>
      <div class="contact__item contact__item--email"><svg class="contact__icon-1"><use href="#i-mail"/></svg>information@pexumor.com</div>
    </div>
  </section>

  <!-- Open end envelope -->
  <section class="sheet sheet--glow sheet--lifted" style="left:148px;top:1897px;width:721px;height:326px">
    <div class="brand brand--on-dark" style="left:64px;top:232px;font-size:34px">PEXUMOR LABS</div>
  </section>

</main>
</body>
</html>
```